KTLwave Power Point Template for Presentations

KTLwave, a leading provider of data to the sports industry is in need of a new look for our Power Point presentations. I added the one we have been using. I want a better cover slide and then a variety of slides that can be used to accommodate bullet points, graphs and charts. I want to stick with our basic color palette of orange and blue as that is the colors we use. I caution you that I don't want to see people playing sports. Our data is used for marketing-oriented analysis and I want that message to come across in a modern and almost fun way. I have attached a report that we did last year. That is what I want to get away from.

```html
<!DOCTYPE html>
<html lang="en">
<head>
<meta charset="utf-8">
<title>KTLwave Presentation Template</title>
<link href="https://fonts.googleapis.com/css2?family=Open+Sans:wght@400;600;700;800&display=swap" rel="stylesheet">
<style>
:root{
  --navy:#2e3a9c;
  --deep:#26318a;
  --orange:#f47920;
  --sky:#1f96d4;
  --grey:#a9a9a9;
  --ink:#333;
  --muted:#777;
  --page:#fff;
}
*{margin:0;padding:0;box-sizing:border-box}
html,body{width:1200px;height:2415px;overflow:hidden}
body{position:relative;font-family:"Open Sans",Arial,sans-serif;color:var(--ink);background:var(--page)}
.stage-top{position:absolute;left:0;top:0;width:1200px;height:1047px;background:linear-gradient(#fff 70%,#f1f1f1)}
.stage-grid{position:absolute;left:0;top:1047px;width:1200px;height:1368px;background:var(--grey)}
.hero{position:absolute;left:95px;top:230px;width:540px;height:304px;transform:scale(1.8704);transform-origin:0 0;box-shadow:0 1px 3px rgba(0,0,0,.15)}
.slide{position:absolute;width:540px;height:304px;background:#fff;overflow:hidden}
.s1{left:51px;top:1090px}.s2{left:608px;top:1090px}
.s3{left:51px;top:1412px}.s4{left:608px;top:1412px}
.s5{left:51px;top:1733px}.s6{left:608px;top:1733px}
.s7{left:51px;top:2055px}.s8{left:608px;top:2055px}
.abs{position:absolute}
.brand{position:absolute;display:flex;align-items:center;gap:4px;color:var(--navy);font-weight:800;line-height:1}
.brand i{display:block;border-radius:50%;background:var(--orange)}
.brand--top{left:26px;top:22px;font-size:24px}
.brand--top i{width:22px;height:22px}
.brand--foot{left:16px;top:280px;font-size:10px}
.brand--foot i{width:9px;height:9px}
.band{position:absolute;left:0;top:77px;width:540px;height:203px;background:linear-gradient(100deg,var(--deep),var(--navy) 60%,#3443a8)}
.cover-title{position:absolute;left:56px;top:120px;color:#fff;font-weight:700;font-size:20px;line-height:24px;letter-spacing:.2px}
.rule{position:absolute;width:20px;height:4px;border-radius:2px;background:var(--orange)}
.cover-sub{position:absolute;left:56px;top:197px;color:#fff;font-size:9.6px}
.cover-date{position:absolute;left:56px;top:236px;color:#fff;font-size:6px}
.cover-foot{position:absolute;left:0;top:286px;width:540px;text-align:center;font-size:7px;color:var(--muted);letter-spacing:.4px}
.cover-foot b{font-weight:700;color:#555}
.copy{position:absolute;right:34px;top:282px;font-size:5px;color:#444}
.pg{position:absolute;right:16px;top:280px;width:9px;height:9px;border-radius:50%;background:var(--navy);color:#fff;font-size:5px;font-weight:700;text-align:center;line-height:9px}
.pg--orange{background:var(--orange)}
.sh{position:absolute;left:23px;top:16px;font-size:17px;color:var(--navy);font-weight:400}
.sh b{font-weight:700}
.sh--orange b{color:var(--orange)}
.sh--blue b{color:var(--navy)}
.sh-rule{left:24px;top:44px}
.tiny{font-size:5px;line-height:6px;color:#666}
.panel{position:absolute;background:var(--navy);color:#fff}
.avatar{position:absolute;width:40px;height:40px;border-radius:50%;background:linear-gradient(#c9cbd3,#8d919e);border:2px solid #fff}
.bio{position:absolute;width:180px;text-align:center;font-size:4.6px;line-height:5.4px;color:#fff}
.strip{position:absolute;left:0;top:175px;width:306px;height:64px;background:var(--sky)}
.strip ul{position:absolute;top:10px;list-style:none;color:#fff;font-size:4.2px;line-height:8px}
.strip li:before{content:"•";margin-right:4px}
.chev{position:absolute;color:var(--orange);font-size:22px;font-weight:700;line-height:1}
.hub-label{position:absolute;font-size:8px;font-weight:700;color:#222;line-height:9px}
.item-h{position:absolute;font-size:9.5px;color:var(--orange)}
.item-h b{font-weight:600}
.dot{position:absolute;width:17px;height:17px;border-radius:50%;background:var(--navy)}
.dot--orange{background:var(--orange)}
.item-p{position:absolute;width:120px;font-size:5px;line-height:6px;color:#666}
.col-h{position:absolute;font-size:9px;color:#222}
.col-h b{font-weight:700}
.bul{position:absolute;list-style:none;font-size:5px;line-height:9.5px;color:#666}
.bul li:before{content:"•";color:var(--orange);margin-right:4px}
.photo{position:absolute;left:272px;top:0;width:134px;height:304px;background:linear-gradient(160deg,#5c5650,#c4bcae 45%,#e6e2da 70%,#a39b8f)}
.leg-h{position:absolute;font-size:9px;font-weight:700;color:#222;display:flex;align-items:center;gap:6px}
.leg-h i{display:block;width:11px;height:11px}
.leg-p{position:absolute;width:135px;font-size:5.2px;line-height:6px;color:#444}
.ring-h{position:absolute;font-size:10px;color:#222}
.ring-h b{font-weight:700}
.ring-p{position:absolute;width:140px;font-size:5px;line-height:6px;color:#666}
.r{text-align:right}
.thanks{position:absolute;left:56px;top:120px;color:#fff;font-size:22px;font-weight:700}
.contact-h{position:absolute;left:56px;top:172px;color:#fff;font-size:9px;font-weight:700}
.contact{position:absolute;left:56px;color:#fff;font-size:7.2px;display:flex;align-items:center;gap:6px}
</style>
</head>
<body>
<div class="stage-top"></div>
<div class="stage-grid"></div>

<!-- featured cover -->
<section class="slide hero" aria-label="Cover slide">
  <div class="brand brand--top"><i></i>KTLwave</div>
  <div class="band" role="img" aria-label="Blue-tinted sports equipment backdrop"></div>
  <h1 class="cover-title">SPORTS FANDOM IN<br>A POST-PANDEMIC WORLD</h1>
  <div class="rule" style="left:57px;top:173px"></div>
  <p class="cover-sub">2021 Annual Study of Sports Fan Habits and Behaviors</p>
  <p class="cover-date">Wednesday, September 18, 2024</p>
  <p class="cover-foot">© 2024 <b>KTLwave.</b> All rights reserved.</p>
</section>

<!-- 1 cover -->
<section class="slide s1" aria-label="Cover slide">
  <div class="brand brand--top"><i></i>KTLwave</div>
  <div class="band" role="img" aria-label="Blue-tinted sports equipment backdrop"></div>
  <h2 class="cover-title">SPORTS FANDOM IN<br>A POST-PANDEMIC WORLD</h2>
  <div class="rule" style="left:57px;top:173px"></div>
  <p class="cover-sub">2021 Annual Study of Sports Fan Habits and Behaviors</p>
  <p class="cover-date">Wednesday, September 18, 2024</p>
  <p class="cover-foot">© 2024 <b>KTLwave.</b> All rights reserved.</p>
</section>

<!-- 2 about -->
<section class="slide s2" aria-label="About us slide">
  <h2 class="sh sh--blue" style="font-weight:600">About Us</h2>
  <div class="rule sh-rule"></div>
  <p class="abs" style="left:24px;top:64px;width:270px;font-size:7.6px;line-height:8.5px;font-weight:700;color:#222">Leading provider of sports market analytics and sports marketing research in the US</p>
  <span class="chev" style="left:24px;top:94px">›</span>
  <p class="abs tiny" style="left:48px;top:96px;width:240px">Comprehensive online platform of nationwide sports marketing analytics, using syndicated and custom research for the professional and college sports, consumer research, industry reports and licensed industry articles.</p>
  <span class="chev" style="left:24px;top:128px">›</span>
  <p class="abs tiny" style="left:48px;top:130px;width:240px">Extensive research and custom reports covering sports participation, the fan market and behaviors, venues, sponsorships and expenditure on sporting goods, brand preference and more.</p>
  <div class="strip">
    <ul style="left:22px"><li>Attendance Analytics</li><li>College Sports Analytics</li><li>Sports Gambling</li><li>Sports Equipment Analytics</li><li>Brand share-of-Market Analytics</li></ul>
    <ul style="left:112px"><li>Logo Apparel Analytics</li><li>Social Media Analytics</li><li>TV Audience Analytics</li><li>Macro Economic DATA</li><li>Sponsorship Influence Analytics</li></ul>
    <ul style="left:202px"><li>Esports Analytics</li><li>Player Analytics</li><li>Fantasy Analytics</li><li>Sports Participation Analytics</li><li>Streaming Audience Analytics</li></ul>
  </div>
  <div class="strip" style="left:306px;width:234px"></div>
  <div class="panel" style="left:306px;top:0;width:214px;height:258px">
    <div class="avatar" style="left:86px;top:32px" role="img" aria-label="Portrait of Dana Whitfield"></div>
    <p class="bio" style="left:17px;top:82px">Dana Whitfield has more than two decades of marketing and consumer research experience in the sports, fitness and active lifestyle categories. She leads the research team and has spoken at many industry conferences and events, and is well respected for her work with leading financial firms and top brands in sports footwear and apparel.</p>
    <div class="avatar" style="left:86px;top:146px" role="img" aria-label="Portrait of Owen Marlowe"></div>
    <p class="bio" style="left:17px;top:198px">Owen Marlowe is a former editor and publisher in sports business and one of the founders of a leading trade show in the category. He now runs a consulting business whose clients include several global companies in the active lifestyle business.</p>
  </div>
  <div class="brand brand--foot"><i></i>KTLwave</div>
  <p class="copy">© 2024 KTLwave. All rights reserved.</p>
  <span class="pg">2</span>
</section>

<!-- 3 six elements -->
<section class="slide s3" aria-label="Six elements slide">
  <svg class="abs" style="left:0;top:0" width="540" height="304" viewBox="0 0 540 304">
    <circle cx="270" cy="153" r="73" fill="none" stroke="#e9e9ec" stroke-width="3"/>
    <circle cx="270" cy="153" r="62" fill="#f6f6f7"/>
    <g fill="#e4e4e7">
      <circle cx="180" cy="62" r="31"/><circle cx="361" cy="62" r="31"/>
      <circle cx="141" cy="153" r="31"/><circle cx="398" cy="153" r="31"/>
      <circle cx="180" cy="243" r="31"/><circle cx="361" cy="243" r="31"/>
    </g>
    <g fill="#e4e4e7">
      <circle cx="215" cy="95" r="4"/><circle cx="326" cy="95" r="4"/>
      <circle cx="190" cy="153" r="4"/><circle cx="350" cy="153" r="4"/>
      <circle cx="215" cy="211" r="4"/><circle cx="326" cy="211" r="4"/>
    </g>
    <circle cx="180" cy="62" r="25" fill="var(--navy)"/>
    <circle cx="361" cy="62" r="25" fill="var(--sky)"/>
    <circle cx="141" cy="153" r="25" fill="var(--orange)"/>
    <circle cx="398" cy="153" r="25" fill="var(--orange)"/>
    <circle cx="180" cy="243" r="25" fill="var(--sky)"/>
    <circle cx="361" cy="243" r="25" fill="var(--navy)"/>
    <g fill="none" stroke="#fff" stroke-width="1.6" stroke-linecap="round">
      <path d="M170 70v-10h20v10M174 58a6 6 0 0 1 12 0"/>
      <rect x="350" y="55" width="16" height="12" rx="2"/><path d="M366 61l7-4v8z"/>
      <rect x="130" y="147" width="22" height="12" rx="5"/><path d="M136 150v6M133 153h6"/>
      <circle cx="398" cy="153" r="10"/><path d="M391 146l14 14"/>
      <circle cx="176" cy="238" r="4"/><circle cx="186" cy="238" r="4"/><path d="M169 252a7 7 0 0 1 14 0M179 252a7 7 0 0 1 14 0"/>
      <circle cx="361" cy="243" r="9"/><path d="M361 237v12M357 240h6"/>
    </g>
    <circle cx="270" cy="120" r="10" fill="var(--navy)"/>
    <text x="270" y="148" text-anchor="middle" font-size="7.4" fill="var(--sky)" font-family="Open Sans, sans-serif">The Six Elements for</text>
    <text x="270" y="157" text-anchor="middle" font-size="7.4" fill="var(--sky)" font-family="Open Sans, sans-serif">Sports Fandom</text>
    <text x="270" y="172" text-anchor="middle" font-size="8" font-weight="800" fill="var(--navy)" font-family="Open Sans, sans-serif">IN A POST</text>
    <text x="270" y="182" text-anchor="middle" font-size="8" font-weight="800" fill="var(--navy)" font-family="Open Sans, sans-serif">PANDEMIC</text>
    <text x="270" y="192" text-anchor="middle" font-size="8" font-weight="800" fill="var(--navy)" font-family="Open Sans, sans-serif">WORLD</text>
  </svg>
  <p class="hub-label" style="left:100px;top:58px">Fandom</p>
  <p class="hub-label" style="left:403px;top:53px">Streaming<br>Media</p>
  <p class="hub-label" style="left:64px;top:149px">E-sports</p>
  <p class="hub-label" style="left:440px;top:145px">Fantasy<br>Sports</p>
  <p class="hub-label r" style="left:80px;top:235px">Social Media<br>Engagement</p>
  <p class="hub-label" style="left:403px;top:235px">Gambling<br>On Sports</p>
  <div class="brand brand--foot"><i></i>KTLwave</div>
  <p class="copy">© 2024 KTLwave. All rights reserved.</p>
  <span class="pg">3</span>
</section>

<!-- 4 four points -->
<section class="slide s4" aria-label="Four point slide">
  <h2 class="sh sh--orange"><b>Heading</b> Goes Here</h2>
  <div class="rule sh-rule"></div>
  <span class="dot" style="left:28px;top:84px"></span>
  <p class="item-h" style="left:62px;top:86px"><b>Heading</b> Goes Here</p>
  <p class="item-p" style="left:62px;top:106px">Lorem ipsum dolor sit amet, consectetur adipiscing elit. Vivamus eu dui ex. Curabitur dapibus dignissim dui, in molestie metus feugiat sed</p>
  <span class="dot" style="left:204px;top:84px"></span>
  <p class="item-h" style="left:238px;top:86px"><b>Heading</b> Goes Here</p>
  <p class="item-p" style="left:238px;top:106px">Lorem ipsum dolor sit amet, consectetur adipiscing elit. Vivamus eu dui ex. Curabitur dapibus dignissim dui, in molestie metus feugiat sed</p>
  <span class="dot" style="left:28px;top:169px"></span>
  <p class="item-h" style="left:62px;top:172px"><b>Heading</b> Goes Here</p>
  <p class="item-p" style="left:62px;top:192px">Lorem ipsum dolor sit amet, consectetur adipiscing elit. Vivamus eu dui ex. Curabitur dapibus dignissim dui, in molestie metus feugiat sed</p>
  <span class="dot" style="left:204px;top:169px"></span>
  <p class="item-h" style="left:238px;top:172px"><b>Heading</b> Goes Here</p>
  <p class="item-p" style="left:238px;top:192px">Lorem ipsum dolor sit amet, consectetur adipiscing elit. Vivamus eu dui ex. Curabitur dapibus dignissim dui, in molestie metus feugiat sed</p>
  <div class="panel" style="left:376px;top:0;width:134px;height:232px;text-align:center">
    <span class="dot dot--orange" style="left:47px;top:36px;width:40px;height:40px"></span>
    <p class="abs" style="left:0;top:88px;width:134px;font-size:13px;line-height:15px"><b>Heading</b><br>Goes Here</p>
    <p class="abs" style="left:14px;top:128px;width:106px;font-size:5.4px;line-height:6.2px">Lorem ipsum dolor sit amet, consectetur adipiscing elit. Vivamus eu dui ex. Curabitur dapibus dignissim dui, in molestie metus feugiat sed. Praesent aliquet lorem ex, eu dapibus odio varius at. Duis eget tellus porta, consequat lacus vitae, venenatis dolor.</p>
  </div>
  <div class="brand brand--foot"><i></i>KTLwave</div>
  <p class="copy">© 2024 KTLwave. All rights reserved.</p>
  <span class="pg">4</span>
</section>

<!-- 5 bullets with image -->
<section class="slide s5" aria-label="Bullet list slide">
  <h2 class="sh sh--orange"><b>Heading</b> Goes Here</h2>
  <div class="rule sh-rule"></div>
  <p class="col-h" style="left:28px;top:80px"><b>Heading</b> Goes Here</p>
  <ul class="bul" style="left:28px;top:96px">
    <li>Praesent aliquet lorem ex, eu dapibus odio varius at.</li>
    <li>Duis eget tellus porta, consequat lacus vitae,</li>
    <li>Dignissim Congue Ut Vitae Magna.</li>
    <li>Phasellus Eget Commodo Arcu.</li>
    <li>Nunc Vitae Semper Dui. Congue Ut Vitae Magna.</li>
  </ul>
  <p class="col-h" style="left:28px;top:174px"><b>Heading</b> Goes Here</p>
  <ul class="bul" style="left:28px;top:190px">
    <li>Praesent aliquet lorem ex, eu dapibus odio varius at.</li>
    <li>Duis eget tellus porta, consequat lacus vitae,</li>
    <li>Dignissim Congue Ut Vitae Magna.</li>
    <li>Phasellus Eget Commodo Arcu.</li>
    <li>Nunc Vitae Semper Dui. Congue Ut Vitae Magna.</li>
  </ul>
  <div class="photo" role="img" aria-label="Photo of hands reviewing printed charts on a desk"></div>
  <div class="panel" style="left:406px;top:0;width:134px;height:304px;background:linear-gradient(160deg,#3441a3,var(--navy))"></div>
  <div class="brand brand--foot"><i></i>KTLwave</div>
  <p class="copy" style="color:#fff">© 2024 KTLwave. All rights reserved.</p>
  <span class="pg pg--orange">5</span>
</section>

<!-- 6 chart -->
<section class="slide s6" aria-label="Chart slide">
  <h2 class="sh sh--blue"><b>Chart</b> Slide Heading</h2>
  <div class="rule sh-rule"></div>
  <svg class="abs" style="left:0;top:0" width="320" height="270" viewBox="0 0 320 270" font-family="Open Sans, sans-serif">
    <g font-size="5" fill="#555" text-anchor="end">
      <text x="50" y="227">0</text><text x="50" y="203">1</text><text x="50" y="179">2</text>
      <text x="50" y="155">3</text><text x="50" y="131">4</text><text x="50" y="107">5</text><text x="50" y="83">6</text>
    </g>
    <line x1="58" y1="225" x2="300" y2="225" stroke="#ccc" stroke-width=".6"/>
    <g font-size="4.6" fill="#444" text-anchor="middle">
      <rect x="67" y="121.8" width="11" height="103.2" fill="var(--navy)"/><text x="72.5" y="119">4.3</text>
      <rect x="81" y="167.4" width="11" height="57.6" fill="var(--orange)"/><text x="86.5" y="164.5">2.4</text>
      <rect x="95" y="177" width="11" height="48" fill="var(--sky)"/><text x="100.5" y="174">2</text>
      <rect x="129" y="165" width="11" height="60" fill="var(--navy)"/><text x="134.5" y="162">2.5</text>
      <rect x="143" y="119.4" width="11" height="105.6" fill="var(--orange)"/><text x="148.5" y="116.5">4.4</text>
      <rect x="157" y="177" width="11" height="48" fill="var(--sky)"/><text x="162.5" y="174">2</text>
      <rect x="191" y="141" width="11" height="84" fill="var(--navy)"/><text x="196.5" y="138">3.5</text>
      <rect x="205" y="181.8" width="11" height="43.2" fill="var(--orange)"/><text x="210.5" y="179">1.8</text>
      <rect x="219" y="153" width="11" height="72" fill="var(--sky)"/><text x="224.5" y="150">3</text>
      <rect x="253" y="117" width="11" height="108" fill="var(--navy)"/><text x="258.5" y="114">4.5</text>
      <rect x="267" y="157.8" width="11" height="67.2" fill="var(--orange)"/><text x="272.5" y="155">2.8</text>
      <rect x="281" y="105" width="11" height="120" fill="var(--sky)"/><text x="286.5" y="102">5</text>
    </g>
    <g font-size="5" fill="#555" text-anchor="middle">
      <text x="86" y="236">Category 1</text><text x="148" y="236">Category 2</text>
      <text x="210" y="236">Category 3</text><text x="272" y="236">Category 4</text>
    </g>
  </svg>
  <p class="leg-h" style="left:345px;top:76px"><i style="background:var(--navy)"></i>Heading 1</p>
  <p class="leg-p" style="left:362px;top:92px">Lorem ipsum dolor sit amet, consectetur adipiscing elit. Vivamus eu dui ex. Curabitur dapibus dignissim dui, in molestie metus feugiat sed.</p>
  <p class="leg-h" style="left:345px;top:134px"><i style="background:var(--orange)"></i>Heading 2</p>
  <p class="leg-p" style="left:362px;top:150px">Lorem ipsum dolor sit amet, consectetur adipiscing elit. Vivamus eu dui ex. Curabitur dapibus dignissim dui, in molestie metus feugiat sed.</p>
  <p class="leg-h" style="left:345px;top:192px"><i style="background:var(--sky)"></i>Heading 3</p>
  <p class="leg-p" style="left:362px;top:208px">Lorem ipsum dolor sit amet, consectetur adipiscing elit. Vivamus eu dui ex. Curabitur dapibus dignissim dui, in molestie metus feugiat sed.</p>
  <div class="brand brand--foot"><i></i>KTLwave</div>
  <p class="copy">© 2024 KTLwave. All rights reserved.</p>
  <span class="pg">6</span>
</section>

<!-- 7 cycle diagram -->
<section class="slide s7" aria-label="Four part cycle slide">
  <h2 class="sh sh--orange"><b>Heading</b> Goes Here</h2>
  <div class="rule sh-rule"></div>
  <svg class="abs" style="left:0;top:0" width="540" height="304" viewBox="0 0 540 304">
    <path d="M270 165V87A78 78 0 0 0 192 165Z" fill="#b8b8bc"/>
    <path d="M270 165V87A78 78 0 0 1 348 165Z" fill="var(--navy)"/>
    <path d="M270 165H192A78 78 0 0 0 270 243Z" fill="var(--sky)"/>
    <path d="M270 165H348A78 78 0 0 1 270 243Z" fill="var(--orange)"/>
    <g stroke="#fff" stroke-width="2"><line x1="270" y1="85" x2="270" y2="245"/><line x1="190" y1="165" x2="350" y2="165"/></g>
    <circle cx="270" cy="165" r="42" fill="#fff"/>
    <circle cx="270" cy="165" r="34" fill="var(--navy)"/>
    <g stroke="#fff" stroke-width="3">
      <circle cx="217" cy="113" r="15" fill="#8d8d92"/>
      <circle cx="323" cy="113" r="15" fill="var(--deep)"/>
      <circle cx="217" cy="217" r="15" fill="#1a84bd"/>
      <circle cx="323" cy="217" r="15" fill="#d9661a"/>
    </g>
  </svg>
  <p class="ring-h r" style="left:40px;top:86px;width:140px"><b>Heading</b> Goes Here</p>
  <p class="ring-p r" style="left:40px;top:101px">Lorem ipsum dolor sit amet, consectetur adipiscing elit. Vivamus eu dui ex. Curabitur dapibus dignissim dui, in molestie metus feugiat sed.</p>
  <p class="ring-h" style="left:364px;top:86px"><b>Heading</b> Goes Here</p>
  <p class="ring-p" style="left:364px;top:101px">Lorem ipsum dolor sit amet, consectetur adipiscing elit. Vivamus eu dui ex. Curabitur dapibus dignissim dui, in molestie metus feugiat sed.</p>
  <p class="ring-h r" style="left:40px;top:193px;width:140px"><b>Heading</b> Goes Here</p>
  <p class="ring-p r" style="left:40px;top:208px">Lorem ipsum dolor sit amet, consectetur adipiscing elit. Vivamus eu dui ex. Curabitur dapibus dignissim dui, in molestie metus feugiat sed.</p>
  <p class="ring-h" style="left:364px;top:193px"><b>Heading</b> Goes Here</p>
  <p class="ring-p" style="left:364px;top:208px">Lorem ipsum dolor sit amet, consectetur adipiscing elit. Vivamus eu dui ex. Curabitur dapibus dignissim dui, in molestie metus feugiat sed.</p>
  <div class="brand brand--foot"><i></i>KTLwave</div>
  <p class="copy">© 2024 KTLwave. All rights reserved.</p>
  <span class="pg">7</span>
</section>

<!-- 8 thank you -->
<section class="slide s8" aria-label="Closing slide">
  <div class="brand brand--top"><i></i>KTLwave</div>
  <div class="band" role="img" aria-label="Blue-tinted sports equipment backdrop"></div>
  <p class="thanks">Thank You!</p>
  <div class="rule" style="left:57px;top:152px"></div>
  <p class="contact-h">Contact Us</p>
  <p class="contact" style="top:196px">
    <svg width="8" height="8" viewBox="0 0 10 10"><path d="M2 1l2 2-1 1.5a6 6 0 0 0 2.5 2.5L7 6l2 2-1.5 1.5C4 9 1 6 .5 2.5Z" fill="#fff"/></svg>555.010-2846</p>
  <p class="contact" style="top:211px">
    <svg width="8" height="8" viewBox="0 0 10 10"><circle cx="5" cy="5" r="4" fill="none" stroke="#fff" stroke-width="1.2"/><circle cx="5" cy="5" r="1.6" fill="none" stroke="#fff" stroke-width="1.2"/></svg>dana@ktlwave.com</p>
  <p class="contact" style="top:226px">
    <svg width="8" height="8" viewBox="0 0 10 10" fill="none" stroke="#fff" stroke-width="1"><circle cx="5" cy="5" r="4"/><ellipse cx="5" cy="5" rx="1.8" ry="4"/><path d="M1 5h8"/></svg>www.ktlwave.com</p>
  <p class="cover-foot">© 2024 <b>KTLwave.</b> All rights reserved.</p>
</section>
</body>
</html>
```